Design einer ITK Unternehmensbroschüre  Grundlayouts mit Deckblatt gesucht
Design einer ITK Unternehmensbroschüre Grundlayouts mit Deckblatt gesucht
Zielgruppe
ITK Systemlösungen mit Schwerpunkt Kommunikationslösungen
Regionale kleine und mittelständische Unternehmen aus allen Branchen
Aufgabenstellung
Vorlage sollte für den Print und Email Versand vorbereitet sein (A4) als Unternehmensbroschüre, die Designlinie sollte bodenständig und innovativ ausgelegt sein.
Dieses Projekt ist als Projektstart zu bewerten und wird in ein eins zu eins Projekt mit erweiterten Budget fortgeführt.
Es soll dazu dienen ein Grundlayout mit Deckblatt zu erstellen um die richtige Linie / Partner zu finden.
Die Kreativität inklusive Aussuchen von passendem Bildmaterial wird vom Designer erwartet und durch Lizenzen im eins zu eins Projekt im Nachgang verrechnet.

```html
<!DOCTYPE html>
<html lang="de">
<head>
<meta charset="utf-8">
<title>velunix – ITK Unternehmensbroschüre</title>
<link rel="stylesheet" href="https://fonts.googleapis.com/css2?family=Hind:wght@300;400;500&display=swap">
<style>
  :root {
    --brand-blue: #14418e;
    --brand-blue-dark: #0e3170;
    --text-dark: #2a2a2a;
    --page-light: #efeff1;
    --page-shade: #dcdcdf;
    --canvas-bg: #ffffff;
    --white: #ffffff;
  }
  * { box-sizing: border-box; margin: 0; padding: 0; }
  html, body {
    width: 1200px; height: 900px; overflow: hidden;
    background: var(--canvas-bg);
    font-family: "Hind", "Helvetica Neue", Arial, sans-serif;
    color: var(--text-dark);
  }
  .page {
    position: absolute;
    width: 372px; height: 538px;
    background: linear-gradient(180deg, var(--page-light), var(--page-shade));
    box-shadow: 0 6px 18px rgba(0,0,0,0.18);
    overflow: hidden;
  }
  .cover { left: 20px; top: 181px; width: 385px; }
  .spread-left { left: 435px; top: 181px; background: linear-gradient(90deg, var(--page-light) 70%, var(--page-shade)); }
  .spread-right { left: 807px; top: 181px; background: linear-gradient(90deg, var(--page-shade), var(--page-light) 30%); }

  .photo { position: absolute; }

  /* Cover */
  .cover-photo {
    left: 0; top: 28px; width: 385px; height: 478px;
    background: linear-gradient(135deg, #3a4f6e 0%, #6d86ad 40%, #a9bad6 70%, #7d95bf 100%);
  }
  .cover-url {
    position: absolute; left: 15px; top: 13px; width: 161px; height: 28px;
    background: var(--brand-blue); color: var(--white);
    font-size: 13px; font-weight: 400; line-height: 30px; padding-left: 11px;
    z-index: 2;
  }
  .cover-title-box {
    position: absolute; left: 0; top: 284px; width: 291px; height: 167px;
    background: var(--brand-blue);
  }
  .cover-title {
    position: absolute; left: 30px; top: 52px;
    color: var(--white); font-size: 18px; font-weight: 300; line-height: 22px;
  }
  .cover-logo-box {
    position: absolute; left: 291px; top: 451px; width: 94px; height: 55px;
    background: var(--white);
    display: flex; align-items: center; justify-content: center; gap: 4px;
  }
  .brand-name {
    color: var(--brand-blue); font-weight: 500; letter-spacing: 0.5px;
  }
  .brand-dot {
    display: inline-block; border-radius: 50%; background: var(--brand-blue);
  }
  .cover-logo-box .brand-name { font-size: 13px; }
  .cover-logo-box .brand-dot { width: 8px; height: 8px; }
  .cover-tagline {
    position: absolute; left: 33px; top: 506px;
    color: var(--brand-blue); font-size: 15px; font-weight: 400; letter-spacing: 0.2px;
  }

  /* Spread shared */
  .page-heading {
    position: absolute; color: var(--brand-blue);
    font-size: 17px; font-weight: 300; line-height: 20px; white-space: nowrap;
  }
  .section-title {
    position: absolute; color: var(--brand-blue);
    font-size: 10px; font-weight: 400; line-height: 12.5px; letter-spacing: 0.3px;
  }
  .body-text {
    position: absolute; text-align: justify; hyphens: auto;
    overflow: hidden; color: var(--text-dark);
  }
  .body-text p + p { margin-top: 0.8em; }

  /* Left page */
  .accent-bar { position: absolute; left: 0; top: 0; width: 31px; height: 175px; background: var(--brand-blue); }
  .security-photo {
    left: 38px; top: 0; width: 334px; height: 175px;
    background: radial-gradient(circle at 55% 50%, #5fa3d8 0%, #1d5a9c 25%, #0b2a57 60%, #061936 100%);
  }
  .telefonie-heading { left: 38px; top: 200px; display: flex; align-items: baseline; gap: 8px; }
  .telefonie-heading .brand-name { font-size: 11px; }
  .telefonie-heading .brand-dot { width: 6px; height: 6px; margin-left: -5px; }
  .telefonie-text {
    left: 38px; top: 224px; width: 291px; height: 112px;
    font-size: 7px; line-height: 9.2px; font-weight: 300;
  }
  .loesungen-left { left: 38px; top: 360px; }
  .ucc-title { left: 38px; top: 388px; }
  .ucc-photo {
    left: 38px; top: 440px; width: 129px; height: 63px;
    background: linear-gradient(160deg, #f2f3f5 0%, #c9cdd4 60%, #a9b0bb 100%);
  }

  /* Right page */
  .loesungen-right { left: 34px; top: 27px; }
  .small-text { font-size: 5.2px; line-height: 6.9px; font-weight: 400; }
  .telefonanlagen-title { left: 34px; top: 53px; }
  .telefonanlagen-text { left: 34px; top: 68px; width: 145px; height: 112px; }
  .phone-photo {
    left: 198px; top: 55px; width: 145px; height: 126px;
    background: linear-gradient(135deg, #8a8d92 0%, #44474c 55%, #2b2d31 100%);
  }
  .voip-photo {
    left: 34px; top: 209px; width: 145px; height: 141px;
    background: linear-gradient(150deg, #a9b0b4 0%, #d7d9dc 40%, #caa48c 75%, #8d7868 100%);
  }
  .isdn-title { left: 199px; top: 208px; width: 145px; }
  .isdn-text { left: 199px; top: 236px; width: 145px; height: 118px; }
  .sip-title { left: 34px; top: 370px; }
  .sip-text { left: 34px; top: 391px; width: 145px; height: 114px; }
  .social-photo {
    left: 199px; top: 372px; width: 145px; height: 133px;
    background: linear-gradient(140deg, #e7ecef 0%, #c9d2d8 50%, #d6b9a4 80%, #9ea7ae 100%);
  }
</style>
</head>
<body>

<section class="page cover" aria-label="Deckblatt">
  <div class="photo cover-photo" role="img" aria-label="Foto: zwei Fachleute im Rechenzentrum vor einer digitalen Bedienoberfläche mit Sicherheitssymbolen"></div>
  <div class="cover-url">www.velunix-itk.de</div>
  <div class="cover-title-box">
    <h1 class="cover-title">Informationstechnologie- und<br>Telekommunikationslösungen</h1>
  </div>
  <div class="cover-logo-box">
    <span class="brand-dot"></span><span class="brand-name">VELUNIX</span>
  </div>
  <p class="cover-tagline">TECHNOLOGISCHE STÄRKEN ERÖFFNEN</p>
</section>

<section class="page spread-left" aria-label="Innenseite links">
  <div class="accent-bar"></div>
  <div class="photo security-photo" role="img" aria-label="Illustration: leuchtendes Vorhängeschloss in digitalen Kreisen auf dunkelblauem Grund"></div>

  <h2 class="page-heading telefonie-heading">TELEFONIE-LÖSUNGEN <span class="brand-dot"></span><span class="brand-name">VELUNIX</span></h2>
  <div class="body-text telefonie-text">
    <p>Als klassischer Systemintegrator bieten wir unseren Kunden eine Vielzahl an hochmodernen sowie konservativen Telekommunikationslösungen an. Wir vereinen die klassische Telefonanlagenstruktur, wie man sie seit Jahrzehnten kennt in den neusten Produktversionen, mit den modernen Voice over IP Telefonanlagen. An einer Umrüstung auf ein modernes Telefonanlagensystem, egal ob bei Ihnen vor Ort oder ausgelagert in einem Rechenzentrum (Cloud/ Private Cloud), werden Sie in den nächsten Jahren nicht herumkommen.</p>
    <p>Wenn es mit der Umrüstung aufgrund der Carrier ISDN Abschaltung schnell gehen muss oder Sie aktuell keine neue Anlage kaufen, mieten oder leasen möchten, dann bieten wir Ihnen schlanke „Überbrückungslösungen“ in Form von Gateway Lösungen an. Diese Lösung spiegelt Ihre aktuelle IST-Situation auf die neue IP Welt, welche von den meisten Netzbetreibern vorausgesetzt wird.</p>
  </div>

  <h2 class="page-heading loesungen-left">Folgende Lösungen bieten wir Ihnen an</h2>
  <h3 class="section-title ucc-title">UNIFIED COMMUNICATIONS<br>UND COLABORATION<br>(UCC) – LÖSUNGEN</h3>
  <div class="photo ucc-photo" role="img" aria-label="Foto: Tastatur mit Taste für Unified Communications"></div>
</section>

<section class="page spread-right" aria-label="Innenseite rechts">
  <h2 class="page-heading loesungen-right">Folgende Lösungen bieten wir Ihnen an</h2>

  <h3 class="section-title telefonanlagen-title">TELEFONANLAGENSYSTEME</h3>
  <div class="body-text small-text telefonanlagen-text">
    <p>Als Spezialist für Telefonielösungen bieten wir unseren Kunden an, die Agilität Ihres Unternehmens zu steigern. Durch den Einsatz von Unified Communications und Collaboration (UCC) -Lösungen verbinden Sie Ihre Teams und Informationen miteinander in Echtzeit und schaffen umfangreiche Möglichkeiten der Zusammenarbeit. Collaboration- und Kommunikationsfunktionen werden in Ihre Anwendungen und Geschäftsprozesse integriert und ermöglichen eine nahtlose, effiziente und gezielte Kommunikation. Diese hochmodernen Kommunikationslösungen ermöglichen eine höhere Effektivität sowie Steigerung der Kommunikation und entlastet viele alt eingewachsene Strukturen. Damit diese Transformation auch erfolgreich verläuft, bieten unsere Experten Ihnen einen sauberen Rollout Plan an und schwören Ihre Mitarbeiter auf persönlichen Schulungen auf das neue System ein.</p>
  </div>
  <div class="photo phone-photo" role="img" aria-label="Foto: Tastenfeld eines Bürotelefons in Nahaufnahme"></div>

  <div class="photo voip-photo" role="img" aria-label="Foto: Hand hält ein VoIP-Mobilteil"></div>
  <h3 class="section-title isdn-title">ISDN – VOICE OVER IP<br>GATEWAYLÖSUNGEN</h3>
  <div class="body-text small-text isdn-text">
    <p>Viele Kunden stehen vor der Herausforderung Ihre alten aber teilweise auch neueren Telefonanlagensysteme von ISDN auf Voice over IP umzurüsten. Viele Carrier haben bereits die herkömmlichen ISDN Anschlüsse abgeschaltet und viele Carrier haben das in den nächsten Jahren noch vor. Nicht selten trifft es einen unvorbereitet und man muss sich schnell entscheiden, da der Carrier mit Kündigung droht!</p>
    <p>Wir bieten unseren Kunden schlanke Gateway Lösungen, welche die aktuelle ISDN Struktur auf IP mittels einem Gateway Router spiegelt und dem aktuellen Carrier signalisiert, dass der Kunde IP spricht. Meistens sind die Kosten für eine solche Lösung weitaus geringer, als in eine Telefonanlage zu investieren, welche in zwei bis drei Jahren aufgrund von Softwareupdates oder möglicherweise End of Life Situationen seitens der Hersteller dann grundsätzlich geändert werden muss. Gerne zeigen wir Ihnen Ihre Möglichkeiten.</p>
  </div>

  <h3 class="section-title sip-title">NETZVERMARKTUNG SIP TRUNK</h3>
  <div class="body-text small-text sip-text">
    <p>Wir bieten kostengünstige und hochverfügbare IP Telefonie Tarife für den individuellen Kunden, welcher sich bei der herkömmlichen Carriern nicht gut aufgehoben fühlt. Die Velunix ist selbst Provider und bietet Ihren Kunden interessante Sprach- sowie -Datenlösungen an. Gerne erstellen wir Ihnen ein passendes Angebot.</p>
    <p>EMPFEHLUNG:</p>
    <p>Wünschen Sie Tarife der herkömmlichen Global Player auf dem Markt, bieten wir über unseren Dienstleistungsgruppen Partner (Torvald Systems) auch Vertragsmanagementlösungen für das Thema Festnetz- sowie Datentarife, Mobilfunk- sowie Vertragsverwaltungslösungen an. Gerne helfen wir Ihnen bei der Brücke zu dem jeweiligen Ansprechpartner, sprechen Sie uns an.</p>
  </div>
  <div class="photo social-photo" role="img" aria-label="Foto: Hand mit Stift vor einem Laptop, darüber schwebende Benachrichtigungssymbole"></div>
</section>

</body>
</html>
```